Coffee Company 1lb coffee bag design

Coffee Bag Design Size ( bag size 12 -16oz / 340 -454 grams / 1lb - dimensions) THE BAG IS GUSSETTED - meaning it has 4sides , like the bags shown in the attachments

* recommend text located at the bottom of the brief added July 9 th

We need a design for a retail 1lb coffee bag to package our Artisan handcrafted roasted coffee beans. The design we choose will be the standard 'look' for our freshly roasted coffee. We have our logo and need to incorporate that into an original, overall design that includes areas for text boxes on the front, back and sides. We have provided a draft of the text at the bottom of the brief to be incorporated in the design. One text box on the front will remain blank. This is where we will adhere a label that will describe the particular coffee in the package. And blank text box on the back to print a bar code.
(Side of the bag : one side of the bag would be our company story (details can be found on our web site) and the other side panel brewing instruction. I would be able to provide the txt for the 'story' and 'brewing instructions' as needed)

These are our preliminary thoughts and are open minded to other options.
We want the design to convey that our coffee is an ethically sourced , locally hand roasted in small batches , freshly roasted, sustainable, socially and environmentally responsible.

This bag will be the our main core bag for use with all the Blends / Roasts so it will need to be starting point for our overall bag design branding. We are very open to all and any creative ideas..
Ideally we would like to use a crisp white gloss bag - the logo would be the main focal point with an area below for where we would place our sticker - roast / blend details .we will be to using a sticker on the front of the bag to identify the various roasts / blends we offer until a point of having a different bag for each coffee. We don't want the bag the appear 'busy' as we prefer images over covering the whole bag with a photo.. the design needs to be crisp , clean , not overall busy, classy , using inspiration perhaps from the logo , twin ridge mountain range , blue ocean, green trees .... our customers enjoy the finer things in life and our brand is more of a luxury product.
Who we are:
We are a Artisan coffee roaster located in the village of Fernhollow. Our hand crafted roasted coffee is ethically sourced , locally roasted in small batches to ensure freshness in every cup. please check out our web site for further details on the company. Again , we are open and looking forward to seeing some fantastic core bag design. we will be looking for the opportunity to develop stickers for each blends in the future...

www.fernhollowcoffeeco.example

attached is the logo files and other bags that have caught our interest ... have some fun!

TEXT FOR: SIDE #1, SIDE #2 , BACK OF THE BAG

FYI - this text is still currently in DRAFT but will allow us to get an overall look for each design...

One side of the coffee bag

Revised draft of the text - updated July19th

THE STORY OF

THE FERNHOLLOW

COFFEE COMPANY,

Nestled beneath the two majestic peaks of the Twin Ridge Mountains along the scenic Cedar Crest highway, is the picturesque village of Fernhollow. This small waterfront community on Vancouver’s North Shore boasts a synchronicity between snowcapped mountains that feed twinkling creeks which meander through lush green forests and lead to the beautiful ocean. This was our inspiration to create Fernhollow Coffee Company and to share our passion for the perfect cup of coffee as reflected in each of our roasts. Our artisan roasted coffee is ethically sourced, using the highest quality Arabica beans then locally roasted in small batches to ensure freshness and the finest flavor. May the coffee you are about to enjoy, enhance your day as you experience the essence of Fernhollow.

-------------------------------------------------

Fernhollow Coffee Company

PO BOX 482

Fernhollow BC

V0K 3R5

the other Side of Bag

KEYS TO BREWING

THE PERFECT CUP

FRESHNESS

Always use freshly roasted (Fernhollow Coffee Company)

beans and within 1-2 weeks of purchase.

STORING

Your coffee has 4 enemies:

Heat, Moisture, Light & Air

Keep your coffee cool, dry and dark in an

airtight container for maximum flavour.

GRINDING

Grind beans just before

brewing. Select the best

grind for each brewing method:

Espresso = Finer Grind

Filtered = Medium Grind

French Press = Coarse Grind

BREWING

Water I Ratio I Temperature

Water: Fresh, cold, filtered water

Ratio: Use 2 rounded tablespoons

of coffee per 8 oz of water.

Temperature: Heat water between 90 – 96 C

Adjust brewing methods to your personal taste.

For more information about

brewing the perfect cup of coffee,

visit our website at

www.fernhollowcoffeeco

(ADD RGBT logo - to be provided)

Back of the bag

"The roasts I create for Fernhollow Coffee Company are a reflection of my commitment to craft the perfect cup of coffee. I hope it is the finest coffee you'll ever enjoy."
- Doran Pettifer,
Founder & Master Roaster, Fernhollow Coffee Company

Visit us our website to learn more including ordering your freshly roasted coffees

(ADD miniature Fernhollow Coffee Company logo)

Like us on Chirpbook

htpp://www.socialpage.example/fernhollowcoffeeco

Follow us on Tweetle

Fernhollow Coffee @fernhollowbrew

send us an email

info@fernhollowcoffeeco.example
Updates

Design Team, just a reminder the bag design is for a gusseted bag ( see brief for details and images ) and not for a pouch bag as what is being submitted to me ? All current designs received so far are the wrong style of bag.

Update effective July 19th, 2014. Please see Brief for revised text for Keys to Brewing, The Story and back side of bag. Thanks.

Reason: Still working with a few designers with text and design - need more time Starting to narrow our selection down soon

Reason: Need to extend to add French to package design

Target Market(s)

coffee drinkers with a mature palate for Arabica Beans , ethically sourced

Industry/Entity Type

It Company

Font styles to use
Other font styles liked:
• same font as logo ?

Colors
0893cd
33a6d7
85cae6
85acd3
3176b5
0455a3
ffffff
cee9f5
eaf1f6

Requirements
Must have
• logo is the main image on front of bag , space for the sticker that will describe the type of bean / roast / blend
Nice to have
• white bag , logo has strong presents front and middle of the bag. crisp clean not busy designs
Should not have
• package should not be 'too busy' it is the core for all roasts and should stand for the roasting company

no cartoon pictures and un authorized clip art

```html
<!DOCTYPE html>
<html lang="en">
<head>
<meta charset="utf-8">
<title>Fernhollow Coffee Company – Gusseted Bag Dieline</title>
<link rel="stylesheet" href="https://fonts.googleapis.com/css2?family=Cinzel:wght@400;700&family=Crimson+Text:wght@400;700&display=swap">
<style>
  :root {
    --bag-blue: #0a56a5;
    --sky-blue: #85cae6;
    --pale-blue: #cee9f5;
    --white: #ffffff;
    --label-grey: #b9b9b9;
    --ink: #1d1d1d;
    --roast-brown: #4b2f1f;
    --tan: #c59b6b;
    --tan-dark: #8a6440;
    --dashes: rgba(255,255,255,0.75);
  }
  * { box-sizing: border-box; margin: 0; padding: 0; }
  html, body { width: 1200px; height: 782px; overflow: hidden; background: var(--white); }
  body { position: relative; font-family: "Crimson Text", Georgia, serif; color: var(--ink); }

  .panel-label {
    position: absolute; top: 66px; width: 200px; margin-left: -100px; text-align: center;
    font-family: Arial, Helvetica, sans-serif; font-size: 13px; letter-spacing: 1px; color: var(--label-grey);
  }

  .dieline { position: absolute; top: 95px; left: 114px; width: 986px; height: 615px; border: 1px solid #d6d6d6; }
  .panel { position: absolute; top: 0; height: 100%; overflow: hidden; }
  .panel--front { left: 0; width: 281px; background: var(--bag-blue); }
  .panel--story { left: 281px; width: 211px; background: var(--bag-blue); color: var(--white); text-align: center; }
  .panel--back  { left: 492px; width: 287px; background: var(--white); text-align: center; }
  .panel--brew  { left: 779px; width: 207px; background: var(--bag-blue); color: var(--white); text-align: center; }

  .rule-ornament { position: absolute; left: 50%; transform: translateX(-50%); }

  /* front */
  .front__band { position: absolute; left: 0; width: 100%; background: var(--sky-blue); }
  .front__band--top { top: 84px; height: 20px; }
  .front__band--bottom { top: 440px; height: 20px; }
  .front__window { position: absolute; left: 0; top: 104px; width: 100%; height: 336px; background: var(--white); }
  .front__logo { position: absolute; left: 0; right: 0; top: 42px; text-align: center; }
  .front__logo-mark { display: block; margin: 0 auto 14px; }
  .brand-name {
    font-family: "Crimson Text", Georgia, serif; font-weight: 700; color: var(--roast-brown);
    letter-spacing: 1px; line-height: 1;
  }
  .front__logo .brand-name { font-size: 36px; }
  .front__roast-label {
    position: absolute; left: 22px; top: 240px; width: 237px; height: 46px;
    background: var(--tan); border: 2px solid var(--tan-dark);
    display: flex; align-items: center; justify-content: center;
    font-family: "Cinzel", Georgia, serif; font-size: 19px; font-weight: 700; color: var(--roast-brown); letter-spacing: 1px;
  }
  .front__weight {
    position: absolute; left: 0; right: 0; top: 500px; text-align: center;
    font-family: "Crimson Text", Georgia, serif; font-size: 15px; color: var(--white);
  }

  /* story side */
  .story__title { margin-top: 55px; font-family: "Cinzel", Georgia, serif; font-size: 10px; line-height: 1.3; letter-spacing: .4px; }
  .story__text { margin: 10px auto 0; width: 150px; font-size: 8px; line-height: 1.3; }
  .story__text p + p { margin-top: 8px; }
  .dash-rule { width: 150px; margin: 20px auto 14px; border-top: 1px dashed rgba(255,255,255,.8); }
  .story__address { font-size: 7.5px; line-height: 1.4; font-style: normal; }
  .story__address + .dash-rule { margin-top: 10px; }
  .story__emblem { display: block; margin: 8px auto 0; }

  /* back */
  .back__logo { position: absolute; left: 0; right: 0; top: 104px; text-align: center; }
  .back__logo .brand-name { font-size: 22px; }
  .back__logo-mark { display: block; margin: 0 auto 8px; }
  .back__lead { position: absolute; top: 264px; left: 0; right: 0; font-size: 13px; line-height: 16px; }
  .back__stars { position: absolute; top: 324px; left: 50%; transform: translateX(-50%); width: 200px; border-top: 2px dotted var(--ink); }
  .back__contact { position: absolute; top: 342px; left: 0; right: 0; font-size: 10px; line-height: 1.3; }
  .back__contact p { margin-bottom: 10px; }

  /* brewing side */
  .brew__title { margin-top: 50px; font-family: "Cinzel", Georgia, serif; font-size: 12px; font-weight: 700; line-height: 1.25; }
  .brew__heading { margin-top: 2px; font-family: "Cinzel", Georgia, serif; font-size: 12px; font-weight: 700; }
  .brew__text { width: 170px; margin: 3px auto 0; font-size: 7.5px; line-height: 1.35; }
  .brew__text + .brew__text { margin-top: 8px; }
  .star-rule { width: 70px; margin: 8px auto 6px; border-top: 1px dotted rgba(255,255,255,.85); }

  .gusset-folds { position: absolute; left: 0; bottom: 0; }
</style>
</head>
<body>

  <div class="panel-label" style="left:255px">FRONT</div>
  <div class="panel-label" style="left:500px">RH SIDE</div>
  <div class="panel-label" style="left:749px">BACK</div>
  <div class="panel-label" style="left:997px">LH SIDE</div>

  <main class="dieline">

    <section class="panel panel--front">
      <svg class="rule-ornament" style="top:52px" width="160" height="10" role="img" aria-label="Decorative flourish rule">
        <rect x="0" y="4" width="160" height="2" fill="#ffffff"/>
      </svg>
      <div class="front__band front__band--top"></div>
      <div class="front__window">
        <div class="front__logo">
          <svg class="front__logo-mark" width="90" height="90" aria-hidden="true">
            <circle cx="45" cy="45" r="43" fill="var(--roast-brown)"/>
          </svg>
          <div class="brand-name">FERNHOLLOW</div>
        </div>
        <div class="front__roast-label">FRENCH ROAST</div>
      </div>
      <div class="front__band front__band--bottom"></div>
      <div class="front__weight">12 oz.</div>
      <svg class="rule-ornament" style="top:527px" width="160" height="10" role="img" aria-label="Decorative flourish rule">
        <rect x="0" y="4" width="160" height="2" fill="#ffffff"/>
      </svg>
    </section>

    <section class="panel panel--story">
      <h2 class="story__title">THE STORY OF THE<br>FERNHOLLOW COFFEE COMPANY</h2>
      <div class="story__text">
        <p>Nestled beneath the two majestic peaks of the Twin Ridge Mountains along the scenic Cedar Crest highway, is the picturesque village of Fernhollow.</p>
        <p>This small waterfront community on Vancouver’s North Shore boasts a synchronicity between snowcapped mountains feeding twinkling creeks meandering through lush green forests and leading to the beautiful ocean.</p>
        <p>This was our inspiration to create the Fernhollow Coffee Company and to share our passion for the perfect cup of coffee as reflected in each of our roasts.</p>
        <p>Our Artisan coffee is ethically sourced, using the highest quality Arabica beans then locally roasted in small batches to ensure freshness and the finest flavor.</p>
        <p>May the coffee you are about to enjoy, enhance your day as you experience the essence of Fernhollow.</p>
      </div>
      <div class="dash-rule"></div>
      <address class="story__address">
        Fernhollow Coffee Company<br>PO BOX 482<br>Fernhollow BC<br>V0K 3R5<br>www.fernhollowcoffeeco.example
      </address>
      <div class="dash-rule"></div>
      <svg class="story__emblem" width="22" height="22" role="img" aria-label="Small fleur emblem">
        <circle cx="11" cy="11" r="9" fill="#ffffff"/>
      </svg>
      <svg class="gusset-folds" width="211" height="180" aria-hidden="true">
        <polyline points="0,180 105,62 211,180" fill="none" stroke="var(--dashes)" stroke-width="1" stroke-dasharray="6 5"/>
      </svg>
    </section>

    <section class="panel panel--back">
      <svg class="rule-ornament" style="top:52px" width="150" height="10" role="img" aria-label="Decorative flourish rule">
        <rect x="0" y="4" width="150" height="2" fill="#1d1d1d"/>
      </svg>
      <div class="back__logo">
        <svg class="back__logo-mark" width="80" height="80" aria-hidden="true">
          <circle cx="40" cy="40" r="38" fill="var(--roast-brown)"/>
        </svg>
        <div class="brand-name">FERNHOLLOW</div>
      </div>
      <p class="back__lead">We hope that you will be inspired<br>by our roasts as much as we were<br>inspired to create them.</p>
      <div class="back__stars"></div>
      <div class="back__contact">
        <p>Visit us our website to learn more including<br>ordering your freshly roasted coffees!</p>
        <p>www.fernhollowcoffeeco.example</p>
        <p>Like us on Chirpbook:<br>htpp://www.socialpage.example/fernhollowcoffeeco</p>
        <p>Follow us on Tweetle:<br>Fernhollow Coffee @fernhollowbrew</p>
        <p>Send us an email:<br>info@fernhollowcoffeeco.example</p>
      </div>
    </section>

    <section class="panel panel--brew">
      <h2 class="brew__title">KEYS TO BREWING<br>THE PERFECT CUP</h2>
      <p class="brew__text">Always try to purchase your coffee<br>at the peak of its freshness.<br>For best results, purchase often and in<br>smaller quantities<br>(1-2 weeks supply max.)</p>
      <div class="star-rule"></div>
      <h3 class="brew__heading">STORING</h3>
      <p class="brew__text">Your coffee has 4 enemies:<br>Heat, Moisture, Light &amp; Air</p>
      <p class="brew__text">Keep your coffee cool, dry and dark in an<br>airtight container for maximum flavour.</p>
      <div class="star-rule"></div>
      <h3 class="brew__heading">GRINDING</h3>
      <p class="brew__text">Grind fresh just before brewing. Select<br>the best grind for each brew method</p>
      <p class="brew__text">Espresso = Finer Grind<br>Drip Coffees = Medium Grind<br>French Press Coffees = Coarse Grind</p>
      <div class="star-rule"></div>
      <h3 class="brew__heading">BREWING</h3>
      <p class="brew__text">Water I Ratio I Temperature<br>Water: Fresh, cold, filtered water<br>Ratio: Use 2 rounded tablespoons<br>of coffee per 8 oz of water<br>Temperature: Heat water between 90 – 96 C</p>
      <p class="brew__text">Adjust brewing methods to your personal taste.</p>
      <div class="star-rule"></div>
      <p class="brew__text">For more information about brewing the<br>perfect cup of coffee, visit our website at<br>www.fernhollowcoffeeco</p>
      <svg class="gusset-folds" width="207" height="180" aria-hidden="true">
        <polyline points="0,180 103,62 207,180" fill="none" stroke="var(--dashes)" stroke-width="1" stroke-dasharray="6 5"/>
      </svg>
    </section>

  </main>
</body>
</html>
```